Welding and farication business card

Business name Tmb Welding & Fabrication

I need a business card made for my welding and fabrication business that is bold and stands out. My business is both welding repairs on machinery and anything else you can imagine as well as fabricating new products. i have used this service before and was very happy with the out come of my design logo. i think the card should remain fairly simple and classy but also be bold. I think a black card would best be suited to the talk with my logo on it. i feel the back of the card should just have my logo and the front have my logo email, website and phone number and maybe incorporate a pagebook and snapgallery simple if it can be made look good these arnt a necessity.
I have included both my logo and some business card ideas below

Target Market(s)

Farmers, heavy industry, earthmoving, trucking

Industry/Entity Type

Engineering

Contact Information for Business Card

0438517264
dane@tmbweldingandfabrication.com.au
www.tmbweldingandfabrication.com.au

Colors
33a6d7
0255a3

Requirements
Must have
• Dane Whitlock
my phone number 0438517264
my logo
Preferably a black card desgn
Nice to have
• List of what i do,
Sheds and carports
Ute trays
Stockyards
Trailers
Farm equipment
Stockcrates
Gateways and Entrances
Breakdowns
Maintenance
And lots more!

```html
<!DOCTYPE html>
<html lang="en">
<head>
<meta charset="utf-8">
<title>Tmb Welding &amp; Fabrication – Business Card</title>
<link href="https://fonts.googleapis.com/css2?family=Montserrat:ital,wght@0,600;0,700;0,800;1,800&family=Oswald:wght@500;700&display=swap" rel="stylesheet">
<style>
  :root {
    --card-black: #050607;
    --brand-blue: #0255a3;
    --deep-blue: #134a93;
    --spark-blue: #33a6d7;
    --white: #ffffff;
    --ink: #0a0a0a;
    --stage: #e8ebed;
    --pattern-black: #121416;
  }
  * { box-sizing: border-box; margin: 0; padding: 0; }
  html, body { width: 1200px; height: 900px; overflow: hidden; }
  body {
    background: var(--stage);
    font-family: "Montserrat", sans-serif;
    position: relative;
  }
  .card {
    position: absolute;
    left: 230px;
    width: 740px;
    height: 420px;
    background: var(--card-black);
    overflow: hidden;
  }
  .card--back { top: 22px; }
  .card--front { top: 458px; }

  /* Back */
  .back-pattern {
    position: absolute; inset: 0;
    background: radial-gradient(ellipse at center, var(--pattern-black) 0%, var(--card-black) 80%);
  }
  .wordmark {
    position: absolute;
    display: flex;
    align-items: center;
    gap: 14px;
    color: var(--white);
    font-weight: 800;
    text-transform: uppercase;
    line-height: 1.05;
  }
  .wordmark__square {
    background: var(--brand-blue);
    flex: none;
  }
  .card--back .wordmark {
    left: 50%; top: 50%;
    transform: translate(-50%, -50%);
    font-size: 34px;
  }
  .card--back .wordmark__square { width: 34px; height: 34px; }
  .wordmark__name small {
    display: block;
    font-size: 0.62em;
    letter-spacing: 0.02em;
  }

  /* Front */
  .card--front .wordmark {
    left: 44px; top: 58px;
    font-size: 30px;
  }
  .card--front .wordmark__square { width: 28px; height: 28px; }

  .front-shape { position: absolute; inset: 0; }

  .name-banner {
    position: absolute;
    left: 36px; top: 250px;
    width: 330px; height: 84px;
    background: var(--white);
    clip-path: polygon(0 0, 100% 0, 88% 100%, 0 100%);
    padding: 10px 0 0 16px;
  }
  .name-banner__name {
    font-family: "Oswald", sans-serif;
    font-weight: 700;
    font-size: 40px;
    line-height: 1;
    text-transform: uppercase;
    color: var(--ink);
    letter-spacing: -0.01em;
  }
  .name-banner__first { color: var(--deep-blue); }
  .name-banner__role {
    margin-top: 6px;
    font-weight: 700;
    font-size: 11px;
    letter-spacing: 0.16em;
    color: var(--ink);
  }

  .phone {
    position: absolute;
    left: 38px; top: 358px;
    display: flex; align-items: center; gap: 12px;
    color: var(--white);
    font-family: "Oswald", sans-serif;
    font-weight: 500;
    font-size: 34px;
    line-height: 1;
  }
  .phone__icon {
    width: 38px; height: 38px;
    background: var(--brand-blue);
    border-radius: 3px;
    display: flex; align-items: center; justify-content: center;
  }

  .services {
    position: absolute;
    left: 545px; top: 180px;
    list-style: none;
    color: var(--white);
    font-weight: 700;
    font-size: 12.5px;
    text-transform: uppercase;
    line-height: 1.32;
  }
  .services li {
    display: flex; align-items: center; gap: 6px;
    margin-bottom: 3px;
  }
  .services li::before {
    content: "";
    width: 0; height: 0;
    border-left: 7px solid var(--white);
    border-top: 6px solid transparent;
    border-bottom: 6px solid transparent;
  }
  .services li.services__more { padding-left: 13px; }
  .services li.services__more::before { display: none; }
</style>
</head>
<body>

<section class="card card--back" aria-label="Card back">
  <div class="back-pattern" role="img" aria-label="Faint repeating company name pattern across the card"></div>
  <div class="wordmark">
    <span class="wordmark__square"></span>
    <span class="wordmark__name">Tmb<small>Welding &amp; Fabrication</small></span>
  </div>
</section>

<section class="card card--front" aria-label="Card front">
  <svg class="front-shape" width="740" height="420" viewBox="0 0 740 420">
    <defs>
      <linearGradient id="torchFill" x1="0" y1="1" x2="1" y2="0">
        <stop offset="0" stop-color="#ffffff"/>
        <stop offset="0.65" stop-color="#e4eff8"/>
        <stop offset="1" stop-color="#33a6d7"/>
      </linearGradient>
    </defs>
    <path d="M480 420 C470 340 480 260 505 200 C520 160 560 130 620 110 L740 60 L740 420 Z" fill="#134a93"/>
    <g role="img" aria-label="Welding torch illustration with a bright blue spark">
      <path d="M385 420 C358 330 382 240 440 190 C490 150 560 118 620 98 L740 38 L740 60 L620 110 C560 130 520 160 505 200 C480 260 470 340 480 420 Z" fill="url(#torchFill)"/>
    </g>
  </svg>

  <div class="wordmark">
    <span class="wordmark__square"></span>
    <span class="wordmark__name">Tmb<small>Welding &amp; Fabrication</small></span>
  </div>

  <div class="name-banner">
    <p class="name-banner__name"><span class="name-banner__first">Dane</span> Whitlock</p>
    <p class="name-banner__role">MANAGING DIRECTOR</p>
  </div>

  <div class="phone">
    <span class="phone__icon">
      <svg width="22" height="22" viewBox="0 0 24 24" aria-hidden="true">
        <path fill="#ffffff" d="M6.6 10.8c1.4 2.8 3.8 5.1 6.6 6.6l2.2-2.2c.3-.3.7-.4 1-.2 1.1.4 2.3.6 3.6.6.6 0 1 .4 1 1V20c0 .6-.4 1-1 1C10.6 21 3 13.4 3 4c0-.6.4-1 1-1h3.5c.6 0 1 .4 1 1 0 1.3.2 2.5.6 3.6.1.3 0 .7-.2 1L6.6 10.8z"/>
      </svg>
    </span>
    <span class="phone__number">0438517264</span>
  </div>

  <ul class="services">
    <li>Sheds &amp; Carports</li>
    <li>Ute Trays</li>
    <li>Stockyards</li>
    <li>Trailers</li>
    <li>Farm Equipment</li>
    <li>Stockcrates</li>
    <li>Gateways &amp; Entrances</li>
    <li>Breakdowns</li>
    <li>Maintenance</li>
    <li class="services__more">And lots more!</li>
  </ul>
</section>

</body>
</html>
```